Upcoming author needs a book cover design (first in a trilogy)

I need a book cover design for my first novel. It is not yet published and I would like to present the book, complete with a cover to potential publishers. In the interim I would like to be able to use the cover as visual motivation to get it published.
The novel is called 'Any Storm, Any Harbour' and my pen name is Marisol Vey. It is a novel set in an Australian beachside town,and is about developing tenacity and courage in the face of fear - aimed at the Young adult market.
I want the cover to be text only (no images) and I really like the old school chalkboard design style. I particularly like the colours turquoise, fuschia pink and canary yellow together. As this is the first of 3 books, I would like the design, fonts and colours to be able to be stepped across all three covers...with one colour used predominently in each cover. For Any Storm, I would like the Turquoise blue to be the strongest colour.
I would like the cover to somehow reflect the fact that the story is set by and in the ocean without appearing 'cute/kitsch' at all.
Updates
Hello Designers,
Target Market(s)
Young adult readers - most books aimed here are black covers with dark print and imagery. I want this to be light, bright and really stand out on the shelves.
Industry/Entity Type
School
Requirements
Must have
- Ability to be printed out as A2
Should not have
- Images

```html
<!DOCTYPE html>
<html lang="en">
<head>
<meta charset="utf-8">
<title>Any Storm, Any Harbour — Cover Concepts</title>
<link rel="stylesheet" href="https://fonts.googleapis.com/css2?family=Federant&family=Zilla+Slab:wght@300&display=swap">
<style>
  :root {
    --page: #ffffff;
    --header: #505050;
    --teal: #2b8ca6;
    --turquoise: #00ccff;
    --turquoise-light: #80e4ff;
    --violet: #6b62d6;
    --fuchsia: #d100ac;
    --coral: #e4596b;
    --canary: #ffcc00;
    --ink-light: #ffffff;
  }
  * { box-sizing: border-box; margin: 0; padding: 0; }
  html, body {
    width: 1200px;
    height: 1000px;
    overflow: hidden;
    background: var(--page);
  }
  .canvas {
    position: relative;
    width: 1200px;
    height: 1000px;
  }
  .cover {
    position: absolute;
    top: 208px;
    width: 421px;
    height: 595px;
    overflow: hidden;
  }
  .cover--plain { left: 115px; }
  .cover--titled { left: 653px; }

  .band {
    position: absolute;
    left: 0;
    width: 100%;
  }
  .band--header { top: 0; height: 45px; background: var(--header); }
  .band--teal { background: var(--teal); }
  .band--turquoise { background: var(--turquoise); }
  .band--violet { background: var(--violet); }
  .band--fuchsia { background: var(--fuchsia); }
  .band--coral { top: 538px; height: 12px; background: var(--coral); }
  .band--canary { top: 550px; height: 45px; background: var(--canary); }

  .author {
    position: absolute;
    left: 14px;
    top: 4px;
    font-family: "Federant", serif;
    font-size: 30px;
    line-height: 36px;
    color: var(--ink-light);
    text-transform: uppercase;
    letter-spacing: 0.5px;
  }

  .moon {
    position: absolute;
    left: 0;
    top: 82px;
    width: 98px;
    height: 196px;
  }

  .title {
    position: absolute;
    right: 14px;
    top: 266px;
    font-family: "Zilla Slab", serif;
    font-weight: 300;
    font-size: 64px;
    line-height: 128px;
    color: var(--ink-light);
    text-align: right;
    white-space: nowrap;
  }
  .title span { display: block; }
</style>
</head>
<body>
<main class="canvas">

  <section class="cover cover--plain" aria-label="Cover colour study">
    <div class="band band--header"></div>
    <p class="author">Marisol Vey</p>
    <div class="band band--teal" style="top:45px;height:11px"></div>
    <div class="band band--turquoise" style="top:56px;height:34px"></div>
    <div class="band band--violet" style="top:90px;height:12px"></div>
    <div class="band band--fuchsia" style="top:102px;height:436px"></div>
    <div class="band band--coral"></div>
    <div class="band band--canary"></div>
  </section>

  <section class="cover cover--titled" aria-label="Front cover: Any Storm, Any Harbour">
    <div class="band band--header"></div>
    <p class="author">Marisol Vey</p>
    <div class="band band--teal" style="top:45px;height:12px"></div>
    <div class="band band--turquoise" style="top:57px;height:437px"></div>
    <svg class="moon" viewBox="0 0 98 196" aria-hidden="true">
      <path d="M0 0 A98 98 0 0 1 0 196 Z" fill="var(--turquoise-light)"/>
    </svg>
    <h1 class="title"><span>Any Storm,</span><span>Any Harbour</span></h1>
    <div class="band band--violet" style="top:494px;height:12px"></div>
    <div class="band band--fuchsia" style="top:506px;height:32px"></div>
    <div class="band band--coral"></div>
    <div class="band band--canary"></div>
  </section>

</main>
</body>
</html>
```